Vietnamese Restaurant Poster

We are a family restaurant specializing in Vietnamese comfort food of pho (Vietnamese Beef Noodle Soup).

We need to create a poster that will attract customers driving by our restaurant.

This poster will be placed on sandwich boards and placed on the intersecting streets.

We want it to be
- big and visually appealing.
- Preferably with a logo incorporating our name and a bowl of Pho
- a arrow sign pointing right
- our phone number 604-318-7915

The name of our restaurant is:

Pho Lanh Tuyet (Title text)
Vietnamese Restaurant (smaller text)

Reason: We have narrowed it down to 2  designs that we absolutely love. Thank you to all who have submitted.

Target Market(s)

Caucasian people who have not tried Vietnamese food. Our location is a little hidden so we want to make these posters to put on the main streets which will grab attention of people driving by to come into our restaurant

Industry/Entity Type

Restaurant

Requirements
Must have
• - big and visually appealing.
logo incorporating our name and a bowl of Pho
Nice to have
• a person eating a bowl of pho

```html
<!DOCTYPE html>
<html lang="en">
<head>
<meta charset="utf-8">
<title>Pho Lanh Tuyet – Vietnamese Restaurant</title>
<link rel="stylesheet" href="https://fonts.googleapis.com/css2?family=Lato:wght@300;400;900&display=swap">
<style>
  :root {
    --poster-red: #9a000f;
    --accent-tan: #cd7b57;
    --title-white: #ffffff;
    --broth-light: #efe6d6;
    --broth-mid: #d9c8aa;
    --herb-green: #5c7a3a;
  }
  html, body {
    margin: 0;
    padding: 0;
    overflow: hidden;
  }
  .poster {
    position: relative;
    width: 801px;
    height: 1200px;
    background: var(--poster-red);
    overflow: hidden;
    font-family: "Lato", sans-serif;
  }
  .restaurant-name {
    position: absolute;
    left: 50px;
    top: 40px;
    margin: 0;
    color: var(--title-white);
    font-family: "Lato", sans-serif;
    font-weight: 900;
    font-size: 152px;
    line-height: 126px;
    letter-spacing: -2px;
    text-transform: uppercase;
  }
  .restaurant-name span {
    display: block;
  }
  .restaurant-type {
    position: absolute;
    left: 52px;
    top: 478px;
    margin: 0;
    color: var(--accent-tan);
    font-family: "Lato", sans-serif;
    font-weight: 300;
    font-size: 70px;
    line-height: 68px;
    letter-spacing: -1px;
    text-transform: uppercase;
  }
  .restaurant-type span {
    display: block;
  }
  .direction-arrow {
    position: absolute;
    left: 568px;
    top: 484px;
    width: 180px;
    height: 132px;
  }
  .dish-photo {
    position: absolute;
    left: 0;
    top: 660px;
    width: 801px;
    height: 372px;
    background:
      radial-gradient(ellipse at 32% 42%, rgba(92,122,58,0.55) 0%, rgba(92,122,58,0) 38%),
      radial-gradient(ellipse at 45% 70%, var(--broth-mid) 0%, rgba(217,200,170,0) 60%),
      linear-gradient(100deg, var(--broth-light) 0%, #f6f1e8 55%, #c9bfae 100%);
  }
  .phone {
    position: absolute;
    left: 52px;
    top: 1054px;
    margin: 0;
    color: var(--accent-tan);
    font-family: "Lato", sans-serif;
    font-weight: 400;
    font-size: 100px;
    line-height: 110px;
    white-space: nowrap;
  }
  .phone-label {
    font-weight: 900;
    margin-right: 10px;
  }
</style>
</head>
<body>
  <main class="poster">
    <h1 class="restaurant-name">
      <span>Pho</span>
      <span>Lanh</span>
      <span>Tuyet</span>
    </h1>

    <p class="restaurant-type">
      <span>Vietnamese</span>
      <span>Restaurant</span>
    </p>

    <svg class="direction-arrow" viewBox="0 0 180 132" aria-label="This way">
      <path d="M14 50 H116 L88 22 A16 16 0 0 1 112 0 L176 58 A12 12 0 0 1 176 74 L112 132 A16 16 0 0 1 88 110 L116 82 H14 A16 16 0 0 1 14 50 Z" fill="var(--accent-tan)"/>
    </svg>

    <div class="dish-photo" role="img" aria-label="Close-up of a white bowl of pho with rice noodles, sliced beef, herbs, chili and lime, with chopsticks resting on the bowl"></div>

    <p class="phone"><span class="phone-label">T</span>604 318 7915</p>
  </main>
</body>
</html>
```